Bobcat / excavator / tipper contractor
info for back of card {
2.3 ton bobcat 1.6m wide
3.6 ton excavator 1.6 wide
4.5M tipper 2.4 wide }
In the industry since 1999
Experienced in all aspects of bobcat excavator general hire work
Brisbane to goldcoast area
competitive rates

As for the image uploaded, I kind of like the H made out of the bulidings and the brown and yellow are the colors of my footy team. but open to anything that is unique the portrays excavation that can become a symbol for my business.so the H is good or something with CTS.

Im wanting to create business cards and either large magnets or a wrap for the front of the truck.
corbintrench @ mailvex . com

Contractor

Reid Corbin
Corbin Trench Services Pty Ltd
ABN 52830174926
mobile 0491286304
corbintrench@mailvex.com

```html
<!DOCTYPE html>
<html lang="en">
<head>
<meta charset="utf-8">
<title>Corbin Trench Services – Business Card</title>
<link href="https://fonts.googleapis.com/css2?family=Arimo:wght@400;700&display=swap" rel="stylesheet">
<style>
  :root {
    --stage: #d8d2c8;
    --card-black: #050505;
    --rust: #9a3f1c;
    --rust-text: #b04a1e;
    --accent-yellow: #e3dc1e;
    --ink-white: #ffffff;
    --muted-white: #e6e6e6;
  }
  * { margin: 0; padding: 0; box-sizing: border-box; }
  html, body {
    width: 1200px; height: 892px; overflow: hidden;
    background: var(--stage);
    font-family: "Arimo", Arial, sans-serif;
  }
  .stage {
    position: relative; width: 1200px; height: 892px;
    display: flex; align-items: center; justify-content: center; gap: 60px;
  }
  .card {
    position: relative; width: 520px; height: 300px;
    background: var(--card-black); overflow: hidden;
    box-shadow: 0 10px 26px rgba(0,0,0,.25);
  }
  /* front */
  .card-front { background: var(--rust); }
  .front-curve { position: absolute; inset: 0; }
  .front-content { position: absolute; left: 150px; right: 30px; top: 48px; }
  .brand-row { display: flex; align-items: center; gap: 12px; }
  .brand-square { width: 18px; height: 18px; background: var(--rust-text); }
  .brand-name {
    color: var(--rust-text); font-weight: 700; font-size: 23px; letter-spacing: .3px;
  }
  .divider { height: 1px; background: var(--accent-yellow); margin: 18px 0 22px; }
  .person-name { color: var(--ink-white); font-size: 26px; }
  .person-role { color: var(--muted-white); font-size: 15px; margin-top: 4px; margin-left: 40px; }
  .contact { margin-top: 26px; color: var(--ink-white); font-size: 15px; line-height: 1.9; }
  /* back */
  .back-company {
    position: absolute; left: 34px; top: 22px; height: 256px;
    writing-mode: vertical-rl; transform: rotate(180deg);
    color: var(--rust-text); font-size: 22px; text-align: center;
  }
  .back-mark {
    position: absolute; left: 150px; top: 0; bottom: 0; right: 30px;
    display: flex; align-items: center; justify-content: center; gap: 18px;
  }
  .back-mark .brand-name { font-size: 92px; }
  .back-mark .brand-square { width: 30px; height: 30px; }
</style>
</head>
<body>
<main class="stage">
  <section class="card card-front" aria-label="Business card front">
    <svg class="front-curve" width="520" height="300" viewBox="0 0 520 300" aria-hidden="true">
      <path d="M520 0 H150 C40 40 40 260 150 300 H520 Z" fill="var(--card-black)"/>
    </svg>
    <div class="front-content">
      <div class="brand-row">
        <span class="brand-square"></span>
        <span class="brand-name">Corbin Trench Services</span>
      </div>
      <div class="divider"></div>
      <p class="person-name">Reid Corbin</p>
      <p class="person-role">Director</p>
      <div class="contact">
        <p>0491286304</p>
        <p>corbintrench@mailvex.com</p>
      </div>
    </div>
  </section>

  <section class="card card-back" aria-label="Business card back">
    <p class="back-company">Corbin Trench Services Pty Ltd</p>
    <div class="back-mark">
      <span class="brand-name">CTS</span>
      <span class="brand-square" style="background: var(--accent-yellow);"></span>
    </div>
  </section>
</main>
</body>
</html>
```